BrixolaV

Hi, We are looking for a design Label for our Packaged Drinking Water. We want a label in rich color. The current Label is uploaded. We wish for a much brighter color rather than black. Our current label is in black. We have attached other company labels to give you idea. The Lomtra bottle image is also uploaded they use sticker for their bottle, front sticker contains name and back sticker's inner portion has graphics and the outer side has information we also open to that.
Industry/Entity Type
Packaged Drinking Water Bottle Brand
Look and feel
Each slider illustrates characteristics of the customer's brand and the style your logo design should communicate.

```html
<!DOCTYPE html>
<html lang="en">
<head>
<meta charset="utf-8">
<title>BrixolaV – Packaged Drinking Water Label</title>
<link href="https://fonts.googleapis.com/css2?family=Oswald:wght@300;400;500;600&display=swap" rel="stylesheet">
<style>
:root{
  --page-top:#e4edeb;
  --page-bottom:#ffffff;
  --label:#7ee6f8;
  --panel:#62ddf9;
  --band:#6ee2f9;
  --accent:#1f74f0;
  --white:#ffffff;
  --ink-cyan:#3cc8ee;
  --art:#6dd6ef;
  --heading:#5cd4f0;
}
*{margin:0;padding:0;box-sizing:border-box}
html,body{width:884px;height:1200px;overflow:hidden}
body{
  position:relative;
  background:linear-gradient(to bottom,var(--page-top) 0%,var(--page-top) 55%,var(--page-bottom) 100%);
  font-family:'Oswald',sans-serif;
  color:var(--white);
}
.board-title{position:absolute;left:21px;top:13px;font-size:12px;font-weight:500;color:var(--heading)}

.label{position:absolute;left:106px;top:140px;width:671px;height:201px;background:var(--label);overflow:hidden}
.label .center-band{position:absolute;left:0;top:97px;width:655px;height:49px;background:var(--band)}
.label .end-tab{position:absolute;left:655px;width:16px;background:var(--accent)}
.label .end-tab.top{top:0;height:27px}
.label .end-tab.bottom{bottom:0;height:28px}
.label .end-strip{position:absolute;left:655px;top:27px;width:16px;height:146px;background:var(--label)}

.mountain-art{position:absolute;left:242px;top:16px;width:166px;height:72px;
  background:radial-gradient(ellipse at 50% 40%,var(--art) 0%,rgba(109,214,239,.35) 60%,rgba(126,230,248,0) 100%)}

.net-qty{position:absolute;left:413px;top:15px;font-size:5.5px;font-weight:500}
.net-qty b{font-size:10px;font-weight:400;margin-left:2px}

.brand{position:absolute;left:231px;top:104px;display:flex;align-items:center;gap:6px}
.brand-name{font-size:34px;font-weight:400;letter-spacing:1px;line-height:1}
.brand-dot{width:26px;height:26px;border-radius:50%;border:5px solid var(--white)}
.product-type{position:absolute;left:0;width:655px;top:168px;text-align:center;font-size:12.5px;font-weight:400;letter-spacing:.3px}

.panel{position:absolute;top:13px;height:172px;background:var(--panel)}
.panel-left{left:19px;width:178px}
.panel-right{left:474px;width:182px}
.t{position:absolute;white-space:nowrap;line-height:1}
.small{font-size:5.4px;font-weight:300}
.caption{font-size:6.6px;font-weight:300}
.company{font-size:8px;font-weight:600}

.cert-mark{position:absolute;left:129px;top:54px;width:27px;height:23px;border:2px solid var(--white);border-radius:3px}
.fssai-box{position:absolute;left:8px;top:93px;width:161px;height:23px;border:1px solid var(--white)}
.fssai-box .badge{position:absolute;left:10px;top:5px;width:38px;height:12px;background:var(--white);opacity:.85;border-radius:2px}
.fssai-box .lic{position:absolute;left:56px;top:6px;font-size:9px;font-weight:400}
.icon-row{position:absolute;left:14px;top:121px;width:150px;display:flex;justify-content:space-between;align-items:center}
.icon-row span{display:block;width:15px;height:15px;background:var(--white);opacity:.9}
.icon-row .round{border-radius:50%}
.crush{position:absolute;left:11px;top:146px;width:160px;height:12px;background:var(--white);color:var(--ink-cyan);font-size:7.5px;font-weight:400;text-align:center;line-height:12px}
.best-before{position:absolute;left:0;width:178px;top:162px;text-align:center;font-size:5.8px;font-weight:500}

.purify{position:absolute;left:8px;top:4px;width:170px;font-size:5.4px;font-weight:300;line-height:8.7px}
.nutri-title{position:absolute;left:8px;top:46px;font-size:7.5px;font-weight:400}
.nutri-title span{font-size:5.6px;font-weight:300}
.nutri{position:absolute;left:8px;top:58px;display:grid;grid-template-columns:47px 47px 60px;row-gap:3.4px;font-size:5.4px;font-weight:300;line-height:5.4px}
.care-box{position:absolute;left:8px;top:88px;width:160px;height:20px;background:var(--white);color:var(--ink-cyan);font-size:5.8px;font-weight:400;padding:3px 3px 0;line-height:7.5px;display:grid;grid-template-columns:66px 1fr}
.notes{position:absolute;left:8px;font-size:5.4px;font-weight:300;line-height:8.6px}
.notes.a{top:113px}
.notes.b{top:142px;line-height:8.5px}

.swatch{position:absolute;left:814px;width:24px;height:24px}
.swatch.s1{top:189px;background:var(--white)}
.swatch.s2{top:219px;background:var(--label)}
.swatch.s3{top:250px;background:var(--panel)}
</style>
</head>
<body>
<div class="board-title">Design #1</div>

<section class="label" aria-label="BrixolaV bottle wrap label">
  <div class="center-band"></div>
  <div class="end-tab top"></div>
  <div class="end-strip"></div>
  <div class="end-tab bottom"></div>

  <div class="mountain-art" role="img" aria-label="Faint mountain peak illustration"></div>
  <div class="net-qty">NET QTY <b>1 L</b></div>
  <div class="brand">
    <span class="brand-name">BRIXOLAV</span>
    <span class="brand-dot"></span>
  </div>
  <div class="product-type">PACKAGED DRINKING WATER</div>

  <div class="panel panel-left">
    <div class="t caption" style="left:8px;top:8px">Manufactured By:</div>
    <div class="t company" style="left:8px;top:19px">Harnil Udyog Pvt Ltd</div>
    <div class="t small" style="left:8px;top:31px">Plot 12, Sector 4, Lalpur, Uttar Pradesh-210001</div>
    <div class="t caption" style="left:8px;top:48px">Marketed By:</div>
    <div class="t company" style="left:8px;top:58px">Kestrova</div>
    <div class="t small" style="left:8px;top:70px">Second Floor, Lakeview Colony, Nandpur,</div>
    <div class="t small" style="left:8px;top:79px">Uttar Pradesh-210002</div>
    <div class="t caption" style="left:131px;top:45px">IS 14543</div>
    <div class="cert-mark" role="img" aria-label="Standards certification mark"></div>
    <div class="t caption" style="left:119px;top:80px">CM/L-5500112233</div>
    <div class="fssai-box">
      <span class="badge" role="img" aria-label="Food licence badge"></span>
      <span class="lic">Lic. No. : 10020030040050</span>
    </div>
    <div class="icon-row" role="img" aria-label="Disposal, recycling and certification marks">
      <span></span><span class="round"></span><span class="round"></span><span></span><span></span><span class="round"></span>
    </div>
    <div class="crush">CRUSH THE BOTTLE AFTER USE</div>
    <div class="best-before">BEST BEFORE 6 MONTHS FROM PACKAGING</div>
  </div>

  <div class="panel panel-right">
    <p class="purify">Every Drop Of BrixolaV Water Goes Through A Multistage Purification Process That Includes Micron Filtration, Purification, UV, Ozonation And With Add Minerals (Calcium Chloride, Magnesium Sulphate &amp; Potassium Bicarbonate).</p>
    <div class="nutri-title">Nutritional Information <span>(Typical values per 100ml) :</span></div>
    <div class="nutri">
      <span>Energy: 0 Kcal</span><span>Protein: 0 g</span><span>Carbohydrate: 0 g</span>
      <span>Calcium: 1.0 mg</span><span>Sugar: 0 g</span><span>Magnesium: 0.5mg</span>
      <span>Fat: 0 g</span><span>Potassium: 0.1 mg</span><span></span>
    </div>
    <div class="care-box">
      <span>Customer Care:</span><span>+91-7000000123</span>
      <span>Email:</span><span>care@harniludyog.com</span>
    </div>
    <p class="notes a">For BIS Certification details, visit:www.stdcheck.in<br>For Date of Manufacturing, Date of Packaging, Batch No.,<br>MRP(Incl. Of All Taxes), Usp &amp; Expiry: CHECK BOTTLE NECK/CAP</p>
    <p class="notes b">Do not accept if Cap/Seal is broken.<br>Store in Cool, Dry &amp; Hygienic place.<br>Keep the container away from direct sunlight.</p>
  </div>
</section>

<div class="swatch s1"></div>
<div class="swatch s2"></div>
<div class="swatch s3"></div>
</body>
</html>
```